Consulting and investment firm, logo design is needed as well.

I am looking to open a consulting firm. Where myself is currently an investor, entrepreneur and consultant for many businesses.

The company name is Morvik Company Limited
The logo should communicate prestige like luxury or gold or money, trustworthy and modern.

Overall name card Color can be: white, black, blue, gold, silver (you can choose one, few or all of it, up to you)

It would be great if you can provide raw file like .psd for me so that I can make some little amendment in future and inserting company name or remove it. Because I would also like to use it as only under my name too (some card I will remove the company name).

• I want it to look modern.

```html
<!DOCTYPE html>
<html lang="en">
<head>
<meta charset="utf-8">
<title>Morvik Company Limited – Business Card</title>
<link rel="stylesheet" href="https://fonts.googleapis.com/css2?family=Outfit:wght@400;500;600&display=swap">
<style>
  :root {
    --brand-blue: #135291;
    --paper: #ffffff;
    --ink-light: #ffffff;
  }
  * { box-sizing: border-box; margin: 0; padding: 0; }
  html, body {
    width: 1200px;
    height: 667px;
    overflow: hidden;
    background: var(--paper);
  }
  .card {
    position: relative;
    width: 1200px;
    height: 667px;
    background: var(--paper);
    font-family: "Outfit", sans-serif;
  }

  /* Brand side */
  .brand {
    position: absolute;
    left: 0;
    top: 0;
    width: 582px;
    height: 667px;
  }
  .brand-mark {
    position: absolute;
    left: 242px;
    top: 236px;
    width: 134px;
    height: 134px;
    background: var(--brand-blue);
  }
  .brand-name {
    position: absolute;
    left: 0;
    top: 430px;
    width: 618px;
    text-align: center;
    color: var(--brand-blue);
    font-size: 44px;
    font-weight: 500;
    line-height: 1.2;
    white-space: nowrap;
  }

  /* Contact side */
  .contact-panel {
    position: absolute;
    left: 582px;
    top: 0;
    width: 618px;
    height: 667px;
    background: var(--brand-blue);
    color: var(--ink-light);
  }
  .owner {
    position: absolute;
    right: 40px;
    top: 50px;
    text-align: right;
  }
  .owner-name {
    font-size: 47px;
    font-weight: 500;
    line-height: 1.1;
  }
  .owner-title {
    font-size: 28px;
    font-weight: 500;
    line-height: 1.2;
  }
  .contact-list {
    list-style: none;
  }
  .contact-item {
    position: absolute;
    left: 50px;
    display: flex;
    align-items: center;
    font-size: 31px;
    font-weight: 500;
  }
  .contact-item svg {
    width: 40px;
    height: 44px;
    margin-right: 52px;
    flex-shrink: 0;
  }
  .contact-phone { top: 261px; }
  .contact-address { top: 364px; }
  .contact-email { top: 476px; }
</style>
</head>
<body>
<main class="card">
  <section class="brand">
    <div class="brand-mark" aria-hidden="true"></div>
    <h1 class="brand-name">Morvik Company Limited</h1>
  </section>

  <section class="contact-panel">
    <header class="owner">
      <p class="owner-name">Owner Name</p>
      <p class="owner-title">Managing Director</p>
    </header>

    <ul class="contact-list">
      <li class="contact-item contact-phone">
        <svg viewBox="0 0 40 44" aria-hidden="true">
          <rect x="10" y="2" width="20" height="40" rx="3" fill="none" stroke="#fff" stroke-width="3"/>
          <line x1="10" y1="9" x2="30" y2="9" stroke="#fff" stroke-width="2"/>
          <line x1="10" y1="35" x2="30" y2="35" stroke="#fff" stroke-width="2"/>
        </svg>
        <span>1234567890</span>
      </li>
      <li class="contact-item contact-address">
        <svg viewBox="0 0 40 44" aria-hidden="true">
          <path d="M20 2C12 2 6 8 6 16c0 10 14 26 14 26s14-16 14-26C34 8 28 2 20 2z" fill="#fff"/>
          <circle cx="20" cy="16" r="5" fill="#135291"/>
        </svg>
        <span>Address 1, Address 2</span>
      </li>
      <li class="contact-item contact-email">
        <svg viewBox="0 0 40 44" aria-hidden="true">
          <rect x="2" y="10" width="36" height="24" fill="none" stroke="#fff" stroke-width="3"/>
          <polyline points="2,10 20,25 38,10" fill="none" stroke="#fff" stroke-width="3"/>
          <line x1="2" y1="34" x2="15" y2="21" stroke="#fff" stroke-width="2.5"/>
          <line x1="38" y1="34" x2="25" y2="21" stroke="#fff" stroke-width="2.5"/>
        </svg>
        <span>info@morvikco.com</span>
      </li>
    </ul>
  </section>
</main>
</body>
</html>
```